Maple Hollow Canine Massage Needs a Business Card Design

Maple Hollow Canine Massage is a new therapeutic canine massage company located in Nederland, Colorado. I need a business card design that include my logo and basic contact information.

Target Market(s)

Pet owners, veterinarians

Industry/Entity Type

Business

Contact Information for Business Card

Lydia Ferrow, CCMT
303.518.7269
lydia@maplehollowmassage.example
www.maplehollowmassage.example

Colors
6c459b
886aae
b8a6cd
a64599
b768aa
d3a5cc
fbed22

Requirements
Must have
• Font should be similar to font in logo.

```html
<!DOCTYPE html>
<html lang="en">
<head>
<meta charset="utf-8">
<title>Maple Hollow Canine Massage – Business Card</title>
<link rel="stylesheet" href="https://fonts.googleapis.com/css2?family=Source+Sans+3:wght@400;600&display=swap">
<style>
  :root {
    --stage: #111111;
    --card: #ffffff;
    --band-top: #e2d8ec;
    --band-bottom: #c3b1d9;
    --logo-fill: #b38fc9;
    --logo-ring: #f5e27a;
    --logo-text: #fbed22;
    --title: #c0a9d8;
    --name: #cd95c8;
    --contact: #c28bbf;
    --icon-bg: #bba6d1;
    --icon-fg: #ffffff;
  }
  * { margin: 0; padding: 0; box-sizing: border-box; }
  html, body {
    width: 1200px; height: 904px; overflow: hidden;
    background: var(--stage);
    font-family: "Source Sans 3", "Myriad Pro", sans-serif;
  }
  .business-card {
    position: absolute; left: 50px; top: 140px;
    width: 1100px; height: 625px;
    background: var(--card);
    overflow: hidden;
  }
  .side-band { position: absolute; inset: 0; }
  .brand-mark {
    position: absolute; left: 79px; top: 67px;
    width: 296px; height: 296px; border-radius: 50%;
    background: var(--logo-fill);
    border: 5px solid var(--logo-ring);
    box-shadow: 0 0 0 18px var(--card);
    display: flex; align-items: center; justify-content: center;
    text-align: center;
  }
  .brand-mark span {
    color: var(--logo-text); font-weight: 600;
    font-size: 30px; line-height: 1.1; width: 220px;
  }
  .card-details {
    position: absolute; right: 60px; top: 0;
    text-align: right;
  }
  .company-name {
    position: absolute; right: 0; top: 196px; white-space: nowrap;
    font-size: 48px; font-weight: 400; color: var(--title);
  }
  .person-name {
    position: absolute; right: 0; top: 342px; white-space: nowrap;
    font-size: 42px; font-weight: 400; color: var(--name);
  }
  .contact-list {
    position: absolute; right: 0; top: 428px; list-style: none;
  }
  .contact-list li {
    display: flex; align-items: center; justify-content: flex-end;
    gap: 33px; height: 44.5px;
    font-size: 31px; color: var(--contact); white-space: nowrap;
  }
  .contact-icon { width: 37px; height: 37px; flex: none; }
</style>
</head>
<body>
  <article class="business-card">
    <svg class="side-band" width="1100" height="625" viewBox="0 0 1100 625" aria-hidden="true">
      <defs>
        <linearGradient id="bandGradient" x1="0" y1="0" x2="0" y2="1">
          <stop offset="0" stop-color="var(--band-top)"/>
          <stop offset="1" stop-color="var(--band-bottom)"/>
        </linearGradient>
      </defs>
      <path d="M0 0 H246 C150 200 110 420 231 625 H0 Z" fill="url(#bandGradient)"/>
    </svg>

    <div class="brand-mark" role="img" aria-label="Maple Hollow Canine Massage logo">
      <span>Maple Hollow Canine Massage</span>
    </div>

    <div class="card-details">
      <h1 class="company-name">Maple Hollow Canine Massage</h1>
      <p class="person-name">Lydia Ferrow, CCMT</p>
      <ul class="contact-list">
        <li>303.518.7269
          <svg class="contact-icon" viewBox="0 0 37 37" aria-label="Phone">
            <rect width="37" height="37" fill="var(--icon-bg)"/>
            <path d="M8 15 Q18.5 7 29 15 L27 18 L23 17 L22 14 Q18.5 13 15 14 L14 17 L10 18 Z" fill="var(--icon-fg)"/>
            <rect x="11" y="19" width="15" height="10" rx="2" fill="var(--icon-fg)"/>
          </svg>
        </li>
        <li>lydia@maplehollowmassage.example
          <svg class="contact-icon" viewBox="0 0 37 37" aria-label="Email">
            <rect width="37" height="37" fill="var(--icon-bg)"/>
            <rect x="7" y="10" width="23" height="17" fill="none" stroke="var(--icon-fg)" stroke-width="2"/>
            <path d="M7 10 L18.5 20 L30 10 M7 27 L15 18 M30 27 L22 18" fill="none" stroke="var(--icon-fg)" stroke-width="1.6"/>
          </svg>
        </li>
        <li>www.maplehollowmassage.example
          <svg class="contact-icon" viewBox="0 0 37 37" aria-label="Website">
            <rect width="37" height="37" fill="var(--icon-bg)"/>
            <circle cx="18.5" cy="18.5" r="10" fill="var(--icon-fg)"/>
            <path d="M13 13 Q17 12 18 16 Q15 19 16 23 Q12 21 13 13 Z M21 20 Q25 19 26 22 Q24 26 21 25 Z" fill="var(--icon-bg)"/>
          </svg>
        </li>
      </ul>
    </div>
  </article>
</body>
</html>
```